Redesign of the Molvekraut label

I am a pharmacist and sell a bitters called "Molvekraut". I would like to revise and modernize the current logo of my "Molvekraut". I have attached a photo of the current label. I have different bottle sizes with different label sizes, but for now I will only need one label for the 700ml size:
20ml 36x47mm
40ml 45x62mm
200ml 70x91mm
350ml 70x98mm
500ml 70x110mm
700ml 87x119mm
The Molve is a small stream that runs through our town. The Molvekraut is a play on words that takes up the mysticism of the Harz, as a spirit can of course also be a schnapps. I like the mysticism and rough nature of the Harz in connection with the product. I have attached a logo suggestion that I once had an AI design. But I am very open to new ideas. A connection to my pharmacy does not necessarily have to be recognizable. VG, K. Harmsen

Target Market(s)

End consumers, gastronomy, restaurants, hotels

```html
<!DOCTYPE html>
<html lang="de">
<head>
<meta charset="utf-8">
<title>Molvekraut Bitterlikör – Etikett 700 ml</title>
<link rel="stylesheet" href="https://fonts.googleapis.com/css2?family=Bodoni+Moda:wght@400;500;600;700&family=Barlow:wght@400&family=Pinyon+Script&family=Nunito+Sans:wght@400&display=swap">
<style>
  :root {
    --paper: #f1e9df;
    --sand: #cdb38f;
    --meadow: #9c8a68;
    --earth: #5b4b40;
    --shadow: #3b302b;
    --heading-brown: #8b786b;
    --ink: #231f1d;
    --badge: rgba(255, 255, 255, 0.96);
  }
  * { margin: 0; padding: 0; box-sizing: border-box; }
  html, body { width: 752px; height: 1200px; overflow: hidden; background: var(--paper); }
  .label {
    position: relative;
    width: 752px;
    height: 1200px;
    overflow: hidden;
    background: var(--paper);
  }
  .landscape {
    position: absolute;
    inset: 0;
    background:
      radial-gradient(ellipse 150px 220px at 375px 980px, rgba(246,240,232,0.95), rgba(246,240,232,0) 100%),
      radial-gradient(ellipse 220px 300px at 60px 1050px, rgba(59,48,43,0.75), rgba(59,48,43,0) 100%),
      radial-gradient(ellipse 220px 300px at 700px 1020px, rgba(59,48,43,0.75), rgba(59,48,43,0) 100%),
      linear-gradient(to bottom,
        #f0e7dc 0px, #ece2d5 230px, #b9a384 330px, #c9b089 420px,
        #a7966f 620px, #8c7c62 780px, #e4dbcf 900px, #d8ccbc 1200px);
  }
  .pharmacy-line {
    position: absolute; left: 0; right: 0; top: 56px;
    text-align: center;
    font-family: "Bodoni Moda", serif;
    font-weight: 600;
    font-size: 27px;
    color: var(--heading-brown);
  }
  .town-line {
    position: absolute; left: 0; right: 0; top: 103px;
    text-align: center;
    font-family: "Barlow", sans-serif;
    font-size: 21px;
    letter-spacing: 5px;
    color: var(--heading-brown);
  }
  .badge {
    position: absolute;
    left: 108px; top: 310px;
    width: 538px; height: 538px;
    border-radius: 50%;
    background: var(--badge);
  }
  .badge-arc { position: absolute; left: 0; top: 0; }
  .arc-text {
    font-family: "Bodoni Moda", serif;
    font-weight: 700;
    font-size: 37px;
    letter-spacing: 5px;
    fill: var(--ink);
  }
  .selection-note {
    position: absolute; left: 0; right: 0; top: 160px;
    text-align: center;
    font-family: "Barlow", sans-serif;
    font-size: 22px;
    letter-spacing: 3.5px;
    color: var(--ink);
  }
  .rule {
    position: absolute; left: 49px; width: 438px; height: 1.5px;
    background: var(--ink);
  }
  .rule.top { top: 221px; }
  .rule.bottom { top: 313px; }
  .product-name {
    position: absolute; left: 0; right: 0; top: 230px;
    text-align: center;
    font-family: "Bodoni Moda", serif;
    font-weight: 500;
    font-size: 62px;
    line-height: 74px;
    color: var(--ink);
  }
  .product-type {
    position: absolute; left: 0; right: 0; top: 333px;
    text-align: center; padding-left: 12px;
    font-family: "Barlow", sans-serif;
    font-size: 26px;
    letter-spacing: 12px;
    color: var(--ink);
  }
  .tradition {
    position: absolute; left: 0; right: 0; top: 368px;
    text-align: center;
    font-family: "Pinyon Script", cursive;
    font-size: 25px;
    color: var(--ink);
  }
  .strength {
    position: absolute; left: 0; right: 0; top: 419px;
    text-align: center;
    font-family: "Bodoni Moda", serif;
    font-weight: 500;
    font-size: 26px;
    color: var(--ink);
  }
  .description {
    position: absolute; left: 0; right: 0; top: 896px;
    text-align: center;
    font-family: "Nunito Sans", sans-serif;
    font-size: 17.5px;
    line-height: 24.4px;
    color: var(--ink);
  }
  .volume {
    position: absolute; left: 0; right: 0; top: 1111px;
    text-align: center;
    font-family: "Bodoni Moda", serif;
    font-weight: 500;
    font-size: 27px;
    color: var(--ink);
  }
</style>
</head>
<body>
<main class="label">
  <div class="landscape" role="img" aria-label="Sepia-Zeichnung einer Harzlandschaft: Himmel mit Vogel, bewaldeter Berg, Fichten, Wiesen und ein Bachlauf mit Gräsern im Vordergrund"></div>

  <p class="pharmacy-line">Aus der St. Lorenz Apotheke</p>
  <p class="town-line">BAD LINDENAU</p>

  <section class="badge">
    <svg class="badge-arc" width="538" height="538" viewBox="0 0 538 538" aria-hidden="true">
      <defs>
        <path id="arc-path" d="M 88 268 A 181 181 0 0 1 450 268"/>
      </defs>
      <text class="arc-text"><textPath href="#arc-path" startOffset="50%" text-anchor="middle">Bad Lindenauer</textPath></text>
    </svg>
    <p class="selection-note">erlesener</p>
    <div class="rule top"></div>
    <h1 class="product-name">MOLVEKRAUT</h1>
    <div class="rule bottom"></div>
    <p class="product-type">BITTERLIKÖR</p>
    <p class="tradition">nach alter Apothekerkunst</p>
    <p class="strength">34% vol</p>
  </section>

  <p class="description">
    Eine Zubereitune nach höchst<br>
    geheinem Rezept.<br>
    Sie sei empfohlen zum Genuss nach<br>
    einem guten Mahl.<br>
    Aufs Feinste zubereitet mit geistigen<br>
    Auszügen von Enzian, Kalmus,<br>
    Malabar-Kardamom und anderen<br>
    wertvollen Zutaten.
  </p>
  <p class="volume">700ml</p>
</main>
</body>
</html>
```